" Já sou fotógrafo e possuo uma marca chamada Otávio Rangel, mais voltada para casamentos, ensaios de casais e família. Todavia já realizei muitos trabalhos no mundo corporativo, como vídeos institucionais de empresas, fotografia gastronômica, foto de carros e vídeos, foto de lojas e estabelecimentos comerciais. Daí que criei a Tulco produções para ser a empresa que irá divulgar esse tipo de material e vender por ela tais produtos de foto e filme. E por ser produções, não se ter;a um limite, poderá oferecer projetos para mídias sociais, campanhas publicitárias e afins. "

```html
<!DOCTYPE html>
<html lang="pt-BR">
<head>
<meta charset="utf-8">
<title>Tulco Produções — Cartão de visita</title>
<link rel="stylesheet" href="https://fonts.googleapis.com/css2?family=Josefin+Sans:wght@300;400&family=Open+Sans:wght@400;600&display=swap">
<style>
  :root {
    --backdrop: #1f1e1e;
    --card-top: #313133;
    --card-bottom: #222224;
    --accent: #3ee62a;
    --text-light: #f2f2f2;
    --text-muted: #8c8c8e;
    --icon-fill: #5a5a5c;
    --icon-ink: #2a2a2c;
  }
  * { margin: 0; padding: 0; box-sizing: border-box; }
  html, body { width: 1200px; height: 1200px; overflow: hidden; }
  body { background: var(--backdrop); position: relative; font-family: "Open Sans", sans-serif; }

  .card {
    position: absolute;
    top: 272px;
    width: 400px;
    height: 725px;
    border-radius: 22px;
    background: linear-gradient(160deg, var(--card-top), var(--card-bottom));
    box-shadow: 0 0 0 1px rgba(255,255,255,0.04);
  }
  .card--front { left: 163px; }
  .card--back { left: 629px; }

  .brand-name {
    position: absolute;
    left: 0; right: 0;
    display: flex;
    justify-content: center;
    align-items: center;
    gap: 14px;
    font-family: "Josefin Sans", sans-serif;
    font-weight: 300;
    color: var(--text-light);
    line-height: 1;
  }
  .brand-name__dot {
    flex: none;
    border-radius: 50%;
    background: var(--accent);
  }

  /* front */
  .brand-name--front { top: 340px; font-size: 40px; }
  .brand-name--front .brand-name__dot { width: 16px; height: 16px; margin-bottom: 6px; }

  /* back */
  .brand-name--back { top: 110px; font-size: 24px; gap: 10px; }
  .brand-name--back .brand-name__dot { width: 11px; height: 11px; margin-bottom: 4px; }

  .person {
    position: absolute;
    left: 0; right: 0;
    top: 180px;
    text-align: center;
  }
  .person__name {
    font-family: "Josefin Sans", sans-serif;
    font-weight: 300;
    font-size: 44px;
    line-height: 1.1;
    color: var(--text-light);
  }
  .person__role {
    margin-top: 6px;
    font-family: "Josefin Sans", sans-serif;
    font-weight: 400;
    font-size: 15px;
    letter-spacing: 5px;
    color: var(--text-light);
  }

  .contact {
    position: absolute;
    display: flex;
    align-items: center;
    gap: 14px;
  }
  .contact__icon {
    flex: none;
    width: 30px; height: 30px;
    border-radius: 50%;
    background: var(--icon-fill);
    display: flex; align-items: center; justify-content: center;
  }
  .contact__icon svg { width: 16px; height: 16px; fill: var(--icon-ink); }
  .contact__text {
    font-size: 10.5px;
    line-height: 1.45;
    color: var(--text-muted);
    text-transform: uppercase;
    letter-spacing: 0.3px;
  }
  .contact--email { left: 118px; top: 373px; }
  .contact--phone { left: 139px; top: 428px; }
  .contact--address { left: 91px; top: 488px; }
  .contact--web { left: 55px; top: 546px; }
</style>
</head>
<body>

<section class="card card--front" aria-label="Frente do cartão">
  <div class="brand-name brand-name--front"><span class="brand-name__dot"></span>Tulco Produções</div>
</section>

<section class="card card--back" aria-label="Verso do cartão">
  <div class="brand-name brand-name--back"><span class="brand-name__dot"></span>Tulco Produções</div>
  <div class="person">
    <div class="person__name">Otávio Rangel</div>
    <div class="person__role">SUPERVISOR</div>
  </div>

  <div class="contact contact--email">
    <span class="contact__icon">
      <svg viewBox="0 0 16 16"><path d="M2 4h12v8H2z M2 4l6 5 6-5" fill="none" stroke="#2a2a2c" stroke-width="1.6"/></svg>
    </span>
    <span class="contact__text">ola@tulcofilmes.com</span>
  </div>

  <div class="contact contact--phone">
    <span class="contact__icon">
      <svg viewBox="0 0 16 16"><path d="M4 2l3 3-1.5 1.5c.8 1.8 2.2 3.2 4 4L11 9l3 3-2 2C7 13 3 9 2 4z"/></svg>
    </span>
    <span class="contact__text">+55 21 3482 7715<br>+55 21 9814 5530</span>
  </div>

  <div class="contact contact--address">
    <span class="contact__icon">
      <svg viewBox="0 0 16 16"><path d="M8 2l6 6h-2v6H9v-4H7v4H4V8H2z"/></svg>
    </span>
    <span class="contact__text">Rua das Laranjeiras 210<br>Rio de Janeiro, RJ</span>
  </div>

  <div class="contact contact--web">
    <span class="contact__icon">
      <svg viewBox="0 0 16 16"><circle cx="8" cy="8" r="5.5" fill="none" stroke="#2a2a2c" stroke-width="1.5"/><path d="M2.5 8h11M8 2.5c2 2 2 9 0 11M8 2.5c-2 2-2 9 0 11" fill="none" stroke="#2a2a2c" stroke-width="1.2"/></svg>
    </span>
    <span class="contact__text">www.tulcofilmes.com</span>
  </div>
</section>

</body>
</html>
```